Harbin Still Works Bottle Label

Harbin Still Works is a distillery and craft cocktail bar that will be located in Calgary, Alberta, Canada. Here, we create awesome hand crafted spirits like vodka, gin, rum, whiskey, brandy, liqueurs etc. We need bottle labels for 3 different initial products. The names of the products are as follows, Pepper Dash Gin (22% alc/vol), Morvane Dry Gin (40% alc/vol), and Talquen Contemporary Gin (40% alc/vol). It would be preferable to have 3 distinct labels. The alcohol by volume declaration must be on the front display of the label, without having to turn the bottle. There is a logo for Harbin Still Works I would like featured in the front around 1''x1" or 2.5cm x 2.5cm in size. Some last minute changes are being made to the logo so it is not uploaded at this moment. Abstract geometry would be a great fit for the contemporary gin and I have attached an example.Simple or complex designs both encouraged. The Pepper Dash Gin will be in the Moonea style bottle and the other two will be in Apotheker style bottles. Thank you so much to anyone interested in participating and we can't wait to hear from you. This is a great opportunity to showcase your creativity and be involved with future products!
Target Market(s)
Young professionals ages 21-30.
Look and feel

```html
<!DOCTYPE html>
<html lang="en">
<head>
<meta charset="utf-8">
<title>Pepper Dash Gin – Bottle Label</title>
<link rel="stylesheet" href="https://fonts.googleapis.com/css2?family=Barlow:wght@500;700;800&family=Black+Ops+One&display=swap">
<style>
  :root {
    --ink: #1e1e1e;
    --paper: #ffffff;
    --stage: #ffffff;
    --navy: #25236a;
    --label-orange: #ee5a2c;
    --dot-orange: #f4a23c;
    --swatch-charcoal: #3a3a3a;
    --swatch-purple: #6b2fa0;
    --swatch-yellow: #f5e400;
    --swatch-rust: #c8491e;
    --swatch-amber: #d9822b;
    --swatch-lime: #c9c31a;
    --swatch-teal: #1a9a8c;
    --label-outline: #c9c9c9;
  }
  * { margin: 0; padding: 0; box-sizing: border-box; }
  html, body { width: 1200px; height: 1200px; overflow: hidden; }
  body {
    background: var(--stage);
    position: relative;
    font-family: "Barlow", Arial, sans-serif;
    color: var(--ink);
  }
  .label {
    position: absolute;
    left: 110px;
    top: 140px;
    width: 456px;
    height: 912px;
    border: 1px solid var(--label-outline);
    background: var(--label-orange);
  }
  .label-head {
    height: 312px;
    background: var(--paper);
    position: relative;
  }
  .logo-square {
    position: absolute;
    left: 170px;
    top: 16px;
    width: 115px;
    height: 115px;
    background: var(--navy);
  }
  .label-head .lockup {
    position: absolute;
    left: 40px;
    top: 130px;
    width: 376px;
  }
  .label-artwork {
    position: absolute;
    left: 34px;
    top: 344px;
    width: 390px;
    height: 470px;
    background: linear-gradient(135deg,
      var(--swatch-yellow) 0%, var(--swatch-amber) 25%,
      var(--swatch-teal) 50%, var(--label-orange) 75%, var(--swatch-purple) 100%);
  }
  .showcase-lockup {
    position: absolute;
    left: 650px;
    top: 640px;
    width: 480px;
  }
  .lockup { display: block; }
  .lockup .place { font-family: "Barlow", Arial, sans-serif; font-weight: 800; font-size: 18px; letter-spacing: 1px; fill: var(--ink); }
  .lockup .product-name { font-family: "Black Ops One", Impact, sans-serif; font-size: 50px; fill: var(--ink); }
  .lockup .detail { font-family: "Barlow", Arial, sans-serif; font-weight: 500; font-size: 22px; fill: var(--ink); }
  .lockup .maker-name { font-family: "Barlow", Arial, sans-serif; font-weight: 700; font-size: 17px; letter-spacing: 2px; fill: var(--ink); }
  .palette {
    position: absolute;
    left: 40px;
    top: 1090px;
  }
  .palette-title {
    font-family: "Barlow", Arial, sans-serif;
    font-weight: 500;
    font-size: 22px;
    letter-spacing: 0.5px;
    color: #333;
    margin-bottom: 10px;
  }
  .palette-swatches { display: flex; gap: 22px; }
  .palette-swatches svg { width: 38px; height: 34px; }
</style>
</head>
<body>

<svg width="0" height="0" style="position:absolute" aria-hidden="true">
  <defs>
    <symbol id="brand-lockup" viewBox="0 0 480 215">
      <text class="place" x="0" y="20">CALGARY</text>
      <text class="place" x="480" y="20" text-anchor="end">CANADA</text>
      <text class="product-name" x="240" y="80" text-anchor="middle" textLength="476" lengthAdjust="spacingAndGlyphs">PEPPER DASH GIN</text>
      <rect x="0" y="92" width="480" height="10" fill="#1e1e1e"/>
      <circle cx="6" cy="136" r="5" fill="#1e1e1e"/>
      <text class="detail" x="18" y="144">22% alc</text>
      <line x1="110" y1="137" x2="172" y2="137" stroke="#1e1e1e" stroke-width="2"/>
      <circle cx="240" cy="138" r="21" fill="#f4a23c"/>
      <line x1="308" y1="137" x2="370" y2="137" stroke="#1e1e1e" stroke-width="2"/>
      <text class="detail" x="462" y="144" text-anchor="end">2018.</text>
      <circle cx="474" cy="136" r="5" fill="#1e1e1e"/>
      <path id="maker-arc" d="M 165 130 A 75 75 0 0 0 315 130" fill="none"/>
      <text class="maker-name"><textPath href="#maker-arc" startOffset="50%" text-anchor="middle">HARBIN STILL WORKS</textPath></text>
    </symbol>
  </defs>
</svg>

<main class="label">
  <section class="label-head">
    <div class="logo-square"></div>
    <svg class="lockup" viewBox="0 0 480 215" role="img" aria-label="Pepper Dash Gin, Calgary Canada, 22% alc, 2018, Harbin Still Works">
      <use href="#brand-lockup"/>
    </svg>
  </section>
  <div class="label-artwork" role="img" aria-label="Abstract geometric artwork of wavy stripes, quarter circles and half circles in yellow, teal, orange, charcoal and purple"></div>
</main>

<svg class="lockup showcase-lockup" viewBox="0 0 480 215" role="img" aria-label="Pepper Dash Gin wordmark lockup">
  <use href="#brand-lockup"/>
</svg>

<section class="palette">
  <p class="palette-title">COLORS</p>
  <div class="palette-swatches">
    <svg viewBox="0 0 38 34"><polygon points="19,4 34,30 4,30" fill="none" stroke="var(--swatch-charcoal)" stroke-width="7" stroke-linejoin="round"/></svg>
    <svg viewBox="0 0 38 34"><polygon points="19,4 34,30 4,30" fill="none" stroke="var(--swatch-purple)" stroke-width="7" stroke-linejoin="round"/></svg>
    <svg viewBox="0 0 38 34"><polygon points="4,4 34,4 19,30" fill="none" stroke="var(--swatch-yellow)" stroke-width="7" stroke-linejoin="round"/></svg>
    <svg viewBox="0 0 38 34"><polygon points="19,4 34,30 4,30" fill="none" stroke="var(--swatch-rust)" stroke-width="7" stroke-linejoin="round"/></svg>
    <svg viewBox="0 0 38 34"><polygon points="19,4 34,30 4,30" fill="none" stroke="var(--swatch-amber)" stroke-width="7" stroke-linejoin="round"/></svg>
    <svg viewBox="0 0 38 34"><polygon points="19,4 34,30 4,30" fill="none" stroke="var(--swatch-lime)" stroke-width="7" stroke-linejoin="round"/></svg>
    <svg viewBox="0 0 38 34"><polygon points="19,4 34,30 4,30" fill="none" stroke="var(--swatch-teal)" stroke-width="7" stroke-linejoin="round"/></svg>
  </div>
</section>

</body>
</html>
```